Menu Design for Indian Restaurant

We are a new Indian restaurant, named Saffron Lantern Restaurant, looking for a sophisticated looking menu. It is a semi-formal dining restaurant with wooden tables and chairs and will have a focus on a creating a lively atmosphere. Environment-friendly products will be used, and the menu will be 100% vegetarian. There will be an emphasis on fresh, healthy and delicious food. We will be targeting vegans, vegetarians, health conscious people, people from all age groups, Indians, Australian's as well as other ethnic communities. We need a clean, simple, sophisticated design for the new restaurant menu. Attached is the restaurant logo for reference.

UPDATE:
- We have attached the menu
- We are not looking for any particular type of layout or size (open to suggests). Please suggest this after having a look at the menu contents. However, we will be having one formal menu to be used in the restaurant, and one in brochure form for distribution.
- There are no images at present. If you feel the need of images, please use sample images for now.

Thank you for the entries thus far.
Updates

Target Market(s)

All age groups from different nationalities

Industry/Entity Type

Indian Restaurant

Colors

Designer to choose colors to be used in the design.

Requirements
Nice to have
• This will be printed on environmentally friendly paper.

```html
<!DOCTYPE html>
<html lang="en">
<head>
<meta charset="utf-8">
<title>Saffron Lantern Restaurant – Punjabi Menu</title>
<link href="https://fonts.googleapis.com/css2?family=Crimson+Text:wght@400;600&family=Mr+Dafoe&display=swap" rel="stylesheet">
<style>
  :root {
    --ink: #3a3130;
    --ink-soft: #4a403d;
    --green: #1f8a3f;
    --saffron: #f6d9a0;
    --peach: #f8d7bf;
    --mint: #d7f1dc;
    --paper: #fffefb;
    --sketch: #b9aba3;
  }
  * { margin: 0; padding: 0; box-sizing: border-box; }
  html, body { width: 848px; height: 1200px; overflow: hidden; }
  body {
    background: var(--paper);
    font-family: "Crimson Text", Georgia, serif;
    color: var(--ink);
  }
  .menu-page {
    position: relative;
    width: 848px;
    height: 1200px;
    overflow: hidden;
    background:
      radial-gradient(ellipse 420px 380px at 640px 120px, var(--saffron) 0%, rgba(246,217,160,0.55) 45%, rgba(246,217,160,0) 100%),
      radial-gradient(ellipse 360px 700px at 820px 640px, var(--peach) 0%, rgba(248,215,191,0.5) 50%, rgba(248,215,191,0) 100%),
      radial-gradient(ellipse 520px 520px at 80px 900px, var(--mint) 0%, rgba(215,241,220,0.6) 50%, rgba(215,241,220,0) 100%),
      radial-gradient(ellipse 380px 300px at 600px 1150px, rgba(215,241,220,0.8) 0%, rgba(215,241,220,0) 100%),
      var(--paper);
  }
  .brand {
    position: absolute;
    top: 108px;
    left: 0;
    width: 848px;
    text-align: center;
    font-family: "Crimson Text", Georgia, serif;
    font-weight: 600;
    color: var(--ink);
    line-height: 1;
  }
  .brand-name { display: block; font-size: 27px; letter-spacing: 0.3px; }
  .brand-sub { display: block; font-size: 10px; letter-spacing: 3px; margin-top: 3px; padding-left: 80px; }
  .section-title {
    position: absolute;
    top: 160px;
    left: 0;
    width: 848px;
    padding-left: 40px;
    text-align: center;
    font-family: "Mr Dafoe", cursive;
    font-weight: 400;
    font-size: 70px;
    color: var(--green);
    line-height: 1;
  }
  .dish-list { position: absolute; list-style: none; }
  .dish-list--left { top: 244px; left: 56px; width: 370px; }
  .dish-list--right { top: 256px; left: 445px; width: 330px; }
  .dish { margin-bottom: 1px; }
  .dish-name {
    font-size: 15px;
    line-height: 19px;
    text-transform: uppercase;
    letter-spacing: 0.2px;
    color: var(--ink);
  }
  .dish-note { font-size: 11px; }
  .dish-price { font-size: 12.5px; margin-left: 2px; }
  .dish-desc {
    font-size: 14px;
    line-height: 18px;
    padding-left: 16px;
    color: var(--ink-soft);
  }
  .produce-illustration {
    position: absolute;
    left: 118px;
    top: 720px;
    width: 660px;
    height: 430px;
  }
</style>
</head>
<body>
<main class="menu-page">
  <header>
    <p class="brand"><span class="brand-name">Saffron Lantern</span><span class="brand-sub">RESTAURANT</span></p>
    <h1 class="section-title">Punjabi</h1>
  </header>

  <ul class="dish-list dish-list--left">
    <li class="dish"><p class="dish-name">Khumb Mattar <span class="dish-price">17.9</span></p><p class="dish-desc">Mushrooms peas tomatoes spice ginger garlic</p></li>
    <li class="dish"><p class="dish-name">Dam Aloo Kasmiri <span class="dish-price">18.9</span></p><p class="dish-desc">Stuffed bake potatoes cashew nut sultana coconut<br>in creamy gravy</p></li>
    <li class="dish"><p class="dish-name">Bhindi Do Pyaz <span class="dish-price">15.9</span></p><p class="dish-desc">Okra made with onion tomato spice ginger garlic</p></li>
    <li class="dish"><p class="dish-name">Kathal Tarkari <span class="dish-note">(SEASONAL)</span> <span class="dish-price">19.9</span></p><p class="dish-desc">Fresh jackfruit cooked with tomatoes ginger garlic<br>fresh coriander</p></li>
    <li class="dish"><p class="dish-name">Baingan Bhartha <span class="dish-price">16.9</span></p><p class="dish-desc">Eggplant pulp tomato fresh coriander ginger garlic</p></li>
    <li class="dish"><p class="dish-name">Paneer Makhani <span class="dish-note">(NUTS)</span> <span class="dish-price">19.9</span></p><p class="dish-desc">Cottage cheese cubes butter sauce nuts<br>cream tomato</p></li>
  </ul>

  <ul class="dish-list dish-list--right">
    <li class="dish"><p class="dish-name">Sarso Ka Sagg <span class="dish-price">15.9</span></p><p class="dish-desc">Fine crushed mustard leafs onion garlic ginger<br>flavoured with mustard oil</p></li>
    <li class="dish"><p class="dish-name">Bagare Baingan <span class="dish-note">(SEASONAL)</span> <span class="dish-price">16.9</span></p><p class="dish-desc">Baby eggplant spiced stuffed tomato ginger garlic</p></li>
    <li class="dish"><p class="dish-name">Vegetable Korma <span class="dish-price">16.9</span></p><p class="dish-desc">Fresh mix vegetable in creamy nut gravy</p></li>
    <li class="dish"><p class="dish-name">Appam Korma <span class="dish-price">16.9</span></p><p class="dish-desc">Fresh mix vegetable coconut milk curry leafs mustard</p></li>
    <li class="dish"><p class="dish-name">Vendakka <span class="dish-price">16.9</span></p><p class="dish-desc">Okra cut, fenugreek seeds, coconut cream,<br>mustard seeds, curry leafs, shallots round</p></li>
    <li class="dish"><p class="dish-name">Bharela Karela <span class="dish-price">16.9</span></p><p class="dish-desc">Bitter gourd stuffed potatoes spice onion ginger<br>garlic serve on gravy</p></li>
  </ul>

  <svg class="produce-illustration" role="img" aria-label="Engraved-style sketch of a wicker basket of beetroots beside a cauliflower and leafy greens" viewBox="0 0 660 430">
    <defs>
      <radialGradient id="produce-tone" cx="50%" cy="55%" r="55%">
        <stop offset="0%" stop-color="#8d7f78" stop-opacity="0.55"/>
        <stop offset="60%" stop-color="#b9aba3" stop-opacity="0.35"/>
        <stop offset="100%" stop-color="#b9aba3" stop-opacity="0"/>
      </radialGradient>
    </defs>
    <rect width="660" height="430" fill="url(#produce-tone)"/>
  </svg>
</main>
</body>
</html>
```